Our companies name is The Gilded Ladle and we specialize in craft cupcakes, what I mean by that is that we bake our cupcakes with craft beer and other alcoholic drinks. We are trying to focus on being elegant but at the same time unpretentious. Since we are incorporating beer in our cupcakes we want the business card to have our logo in the front and our information in the back.

Once we select the best design we will provide the contact information to be added. Thank you.

Industry/Entity Type

Business

Font styles to use
Decorative
Script

Requirements
Must have
• Round corners
Should not have
• Square corners

```html
<!DOCTYPE html>
<html lang="en">
<head>
<meta charset="utf-8">
<title>The Gilded Ladle — Business Card</title>
<link rel="stylesheet" href="https://fonts.googleapis.com/css2?family=Oswald:wght@500&family=Quicksand:wght@500&display=swap">
<style>
  :root {
    --canvas: #ffffff;
    --card-black: #0b0b0b;
    --brand-red: #e8212b;
    --brand-teal: #84d1c6;
    --text-white: #f4f4f4;
    --front-light: #f7f7f7;
    --front-shade: #cfcfcf;
  }
  * { margin: 0; padding: 0; box-sizing: border-box; }
  html, body { width: 1200px; height: 800px; overflow: hidden; background: var(--canvas); }
  .canvas { position: relative; width: 1200px; height: 800px; }

  .card {
    position: absolute;
    top: 245px;
    width: 540px;
    height: 310px;
    border-radius: 18px;
    overflow: hidden;
    box-shadow: 0 6px 18px rgba(0,0,0,.18);
  }

  /* Back: contact side */
  .card-back { left: 40px; background: var(--card-black); }
  .band-red {
    position: absolute; left: 0; top: 0; width: 100%; height: 34px;
    background: var(--brand-red);
  }
  .band-teal { position: absolute; left: 0; bottom: 0; width: 100%; height: 62px; }
  .back-brand {
    position: absolute; left: 28px; top: 92px; width: 220px;
    display: flex; align-items: center; gap: 10px;
  }
  .brand-dot {
    flex: none; width: 22px; height: 22px; border-radius: 50%;
    background: var(--brand-red);
  }
  .brand-name {
    font-family: "Oswald", sans-serif; font-weight: 500;
    color: var(--brand-teal); text-transform: uppercase;
    font-size: 26px; line-height: 1.1; letter-spacing: 1px;
  }
  .divider {
    position: absolute; left: 268px; top: 64px;
    width: 2px; height: 176px; background: var(--text-white);
  }
  .contact { position: absolute; left: 292px; top: 70px; }
  .contact-name {
    font-family: "Oswald", sans-serif; font-weight: 500;
    color: var(--brand-red); font-size: 34px; line-height: 1.05; letter-spacing: 1px;
  }
  .contact-title {
    font-family: "Quicksand", sans-serif; font-weight: 500;
    color: var(--brand-teal); font-size: 13px; letter-spacing: 7px;
    text-transform: uppercase; margin: 4px 0 10px;
  }
  .contact-list { list-style: none; }
  .contact-item {
    display: flex; align-items: center; gap: 10px;
    font-family: "Quicksand", sans-serif; font-weight: 500;
    color: var(--text-white); font-size: 16px; letter-spacing: 1.5px;
    line-height: 26px;
  }
  .contact-icon { width: 16px; height: 16px; flex: none; }

  /* Front: brand side */
  .card-front {
    left: 620px;
    background: radial-gradient(circle at 50% 45%, var(--front-light) 0%, #e6e6e6 55%, var(--front-shade) 100%);
    display: flex; align-items: center; justify-content: center; gap: 14px;
  }
  .card-front .brand-dot { width: 30px; height: 30px; }
  .card-front .brand-name { font-size: 40px; color: var(--card-black); }
</style>
</head>
<body>
<main class="canvas">

  <section class="card card-back" aria-label="Business card, contact side">
    <div class="band-red"></div>
    <svg class="band-teal" viewBox="0 0 540 62" preserveAspectRatio="none" aria-hidden="true">
      <polygon points="0,40 540,0 540,62 0,62" fill="var(--brand-teal)"/>
    </svg>

    <div class="back-brand">
      <span class="brand-dot"></span>
      <span class="brand-name">The Gilded Ladle</span>
    </div>

    <div class="divider"></div>

    <div class="contact">
      <p class="contact-name">Your Name</p>
      <p class="contact-title">Job Title</p>
      <ul class="contact-list">
        <li class="contact-item">
          <svg class="contact-icon" viewBox="0 0 16 16" aria-hidden="true"><path d="M2 4c0-1.5 2.5-2.5 6-2.5s6 1 6 2.5v1.5h-3.2V4H5.2v1.5H2z M4 7h8l2 7H2z" fill="var(--text-white)"/><circle cx="8" cy="10.5" r="1.8" fill="var(--card-black)"/></svg>
          phonenumber
        </li>
        <li class="contact-item">
          <svg class="contact-icon" viewBox="0 0 16 16" aria-hidden="true"><rect x="1" y="3" width="14" height="10" fill="var(--text-white)"/><path d="M1 3l7 6 7-6" fill="none" stroke="var(--card-black)" stroke-width="1.3"/></svg>
          email@
        </li>
        <li class="contact-item">
          <svg class="contact-icon" viewBox="0 0 16 16" aria-hidden="true"><g fill="none" stroke="var(--text-white)" stroke-width="1.2"><circle cx="8" cy="8" r="6.5"/><ellipse cx="8" cy="8" rx="3" ry="6.5"/><path d="M1.5 8h13M2.5 5h11M2.5 11h11"/></g></svg>
          otherinfo
        </li>
      </ul>
    </div>
  </section>

  <section class="card card-front" aria-label="Business card, brand side">
    <span class="brand-dot"></span>
    <span class="brand-name">The Gilded Ladle</span>
  </section>

</main>
</body>
</html>
```